Riverbend Strong Unions and Households Project-Postcard

We need a postcard to promote our program. We will use the postcard to remind clients of appointments or even use it as a marketing tool when we go out to events. We provide healthy relationship education, financial classes and job readiness education. Our target population is adult couples. Mostly Spanish speaking. If its possible to incorporate all three components into the design that would be great, if not, healthy relationship would be our priority.

Attached is a logo we would like to use.

I have also included the text we would like to use. Would you please make all text editable incase we want to add different text.

The funding statement has to go at the bottom (it can be in small text).

Industry/Entity Type

Marketing

Requirements
Must have
• if you use images of people, please use Latino images. Our target population is Spanish speaking.

```html
<!DOCTYPE html>
<html lang="es">
<head>
<meta charset="utf-8">
<title>Riverbend Strong Unions and Households Project – Postcard</title>
<link rel="stylesheet" href="https://fonts.googleapis.com/css2?family=Source+Sans+3:wght@400;600;700&display=swap">
<style>
  :root {
    --bg: #9a9a9a;
    --paper: #ffffff;
    --orange: #f39a1e;
    --orange-deep: #e07b12;
    --charcoal: #3b3b3b;
    --ink: #4a4a4a;
    --navy: #1f3f78;
    --line: #c9c9c9;
  }
  * { box-sizing: border-box; margin: 0; padding: 0; }
  html, body { width: 800px; height: 1200px; overflow: hidden; }
  body { background: var(--bg); font-family: "Source Sans 3", Arial, sans-serif; position: relative; }

  .card { position: absolute; left: 48px; width: 704px; background: var(--paper); overflow: hidden; }
  .card--front { top: 40px; height: 500px; }
  .card--back { top: 580px; height: 570px; }

  .front-photo {
    position: absolute; left: 0; top: 0; width: 100%; height: 300px;
    background: linear-gradient(180deg, #6f6f6f 0%, #a9a9a9 45%, #d8d8d8 80%, #ffffff 100%);
  }
  .front-swoosh { position: absolute; left: 0; top: 0; width: 704px; height: 500px; }
  .front-message { position: absolute; left: 0; top: 248px; width: 100%; text-align: center; }
  .headline { color: var(--orange); font-size: 36px; font-weight: 400; line-height: 1.05; }
  .call { color: var(--ink); font-size: 21px; line-height: 1.15; margin-top: 6px; }
  .call strong { color: var(--navy); font-weight: 700; font-size: 24px; }

  .funding {
    position: absolute; left: 24px; top: 414px; width: 300px;
    font-size: 10px; line-height: 1.3; color: var(--ink);
  }

  .logo-row { position: absolute; display: flex; align-items: center; gap: 18px; }
  .front-logos { right: 24px; top: 420px; }
  .back-logos { left: 28px; top: 496px; }
  .brand { display: flex; align-items: center; gap: 7px; font-size: 12px; font-weight: 600; line-height: 1.15; color: var(--ink); }
  .brand--program { width: 170px; }
  .brand--partner { width: 130px; color: var(--navy); }
  .brand__dot { flex: none; width: 16px; height: 16px; border-radius: 50%; background: var(--orange); }
  .brand__square { flex: none; width: 14px; height: 14px; background: var(--navy); }
  .logo-divider { width: 1px; height: 40px; background: var(--line); }

  .back-panel { position: absolute; left: 0; top: 0; width: 352px; height: 460px; background: var(--charcoal); }
  .pillars { list-style: none; position: absolute; left: 0; top: 30px; width: 352px; }
  .pillar { display: flex; flex-direction: column; align-items: center; height: 136px; }
  .pillar__icon { width: 76px; height: 76px; }
  .pillar__label { color: #fff; font-size: 17px; margin-top: 8px; }

  .stamp { position: absolute; right: 24px; top: 22px; width: 72px; height: 84px; border: 1.5px solid var(--line); }
  .address-lines { position: absolute; left: 420px; top: 300px; width: 260px; }
  .address-lines span { display: block; height: 38px; border-bottom: 1.5px solid var(--line); }
  .back-swoosh { position: absolute; left: 0; top: 0; width: 704px; height: 570px; }
</style>
</head>
<body>

<section class="card card--front" aria-label="Frente de la tarjeta">
  <div class="front-photo" role="img" aria-label="Black and white photo of a couple holding hands on a path"></div>
  <svg class="front-swoosh" viewBox="0 0 704 500" aria-hidden="true">
    <path d="M0 402 C180 388 420 414 704 388 L704 395 C420 421 180 395 0 409 Z" fill="var(--orange)"/>
    <path d="M0 500 L704 500 L704 488 C500 482 300 498 0 492 Z" fill="var(--orange)"/>
  </svg>
  <div class="front-message">
    <p class="headline">…porque una relación<br>sana está a su alcance</p>
    <p class="call">Para más información,<br>llame a <strong>555-014-3556</strong></p>
  </div>
  <p class="funding">“Funding for this project was provided by the Regional Office of Family and Household Services, Grant: #00RB0417. These services are available to all eligible persons, regardless of race, gender, age, disability, or religion.”</p>
  <div class="logo-row front-logos">
    <div class="brand brand--program"><span class="brand__dot"></span>Riverbend Strong Unions and Households Project</div>
    <span class="logo-divider"></span>
    <div class="brand brand--partner"><span class="brand__square"></span>Riverbend Community Partners</div>
  </div>
</section>

<section class="card card--back" aria-label="Reverso de la tarjeta">
  <div class="back-panel">
    <ul class="pillars">
      <li class="pillar">
        <svg class="pillar__icon" viewBox="0 0 76 76" aria-hidden="true">
          <circle cx="38" cy="38" r="38" fill="var(--orange)"/>
          <path d="M38 56 C22 45 18 38 18 31 a9 9 0 0 1 20 -3 a9 9 0 0 1 20 3 c0 7 -4 14 -20 25 Z" fill="#fff"/>
        </svg>
        <span class="pillar__label">Healthy Relationship</span>
      </li>
      <li class="pillar">
        <svg class="pillar__icon" viewBox="0 0 76 76" aria-hidden="true">
          <circle cx="38" cy="38" r="38" fill="var(--orange)"/>
          <path d="M38 14 L28 26 H34 V40 H42 V26 H48 Z" fill="#fff"/>
          <rect x="20" y="44" width="36" height="16" rx="2" fill="#fff"/>
          <text x="38" y="57" text-anchor="middle" font-size="14" font-weight="700" fill="var(--orange)" font-family="Source Sans 3, sans-serif">$</text>
        </svg>
        <span class="pillar__label">Financial Stability</span>
      </li>
      <li class="pillar">
        <svg class="pillar__icon" viewBox="0 0 76 76" aria-hidden="true">
          <circle cx="38" cy="38" r="38" fill="var(--orange)"/>
          <rect x="18" y="30" width="40" height="26" rx="3" fill="#fff"/>
          <path d="M31 30 V24 H45 V30" fill="none" stroke="#fff" stroke-width="4"/>
          <rect x="18" y="40" width="40" height="3" fill="var(--orange)"/>
        </svg>
        <span class="pillar__label">Workforce Readiness</span>
      </li>
    </ul>
  </div>
  <div class="stamp" aria-label="Stamp area"></div>
  <div class="address-lines" aria-label="Address lines"><span></span><span></span><span></span><span></span></div>
  <svg class="back-swoosh" viewBox="0 0 704 570" aria-hidden="true">
    <path d="M0 455 C200 475 420 430 704 470 L704 476 C420 438 200 484 0 463 Z" fill="var(--orange)"/>
    <path d="M0 570 L704 570 L704 552 C500 540 300 566 0 556 Z" fill="var(--orange)"/>
  </svg>
  <div class="logo-row back-logos">
    <div class="brand brand--program"><span class="brand__dot"></span>Riverbend Strong Unions and Households Project</div>
    <span class="logo-divider"></span>
    <div class="brand brand--partner"><span class="brand__square"></span>Riverbend Community Partners</div>
  </div>
</section>

</body>
</html>
```